A simple Facebook Ad (not Facebook Page) for weight loss surgery

It’s a simple ad in terms of the text.

The text should say:
Curious about weight loss surgery?
This 30 second quiz will tell you which procedure will suit you best

I'm open to variations in the text if it is thought to enhance the ad.

Targeted towards obese individuals who have been unable to lose weight with diet and exercise. My industry is weight loss surgery – webpage www.merivalebardsley.com.au. Clicking the ad leads to a quiz on my webpage relating to weight loss surgery. Most frequent users of this service are females (75%) between ages of 35 and 55 years.

Successful weight loss surgery can enable individuals who have been unable to lose weight to lose a substantial amount of the excess weight they are carrying to be healthier and happier.

```html
<!DOCTYPE html>
<html lang="en">
<head>
<meta charset="utf-8">
<title>Merivale Bardsley – Weight Loss Surgery Quiz Ad</title>
<link href="https://fonts.googleapis.com/css2?family=Bebas+Neue&family=Montserrat:wght@300;400;600;700&display=swap" rel="stylesheet">
<style>
  :root {
    --teal: #14998f;
    --teal-deep: #0c746c;
    --teal-light: #3fb1a8;
    --ink-grey: #5d5c62;
    --dark-grey: #3b3b3f;
    --sky-top: #eef3f8;
    --sky-bottom: #dde8f2;
    --white: #ffffff;
  }
  * { margin: 0; padding: 0; box-sizing: border-box; }
  html, body { width: 1200px; height: 1200px; overflow: hidden; }
  body { background: var(--sky-top); font-family: "Montserrat", sans-serif; }

  .ad {
    position: relative;
    width: 1200px;
    height: 1200px;
    overflow: hidden;
    background: linear-gradient(180deg, var(--sky-top) 0%, var(--sky-bottom) 100%);
  }

  .model-photo {
    position: absolute;
    left: 300px;
    top: 26px;
    width: 555px;
    height: 900px;
    border-radius: 240px 240px 60px 60px;
    background:
      linear-gradient(180deg, rgba(230,190,165,0.55) 0%, rgba(238,205,185,0.6) 55%, rgba(110,150,200,0.75) 75%, rgba(95,135,185,0.85) 100%);
  }

  .shapes { position: absolute; inset: 0; width: 1200px; height: 1200px; }

  .brand {
    position: absolute;
    left: 41px;
    top: 46px;
    display: flex;
    align-items: center;
    gap: 16px;
  }
  .brand-dot {
    width: 80px; height: 80px;
    border-radius: 50%;
    background: var(--teal);
  }
  .brand-name {
    font-weight: 600;
    font-size: 31px;
    letter-spacing: 1px;
    color: var(--teal);
    text-transform: uppercase;
    line-height: 1;
    white-space: nowrap;
  }
  .brand-role {
    margin-top: 6px;
    font-weight: 400;
    font-size: 11.5px;
    letter-spacing: 2.2px;
    color: var(--ink-grey);
    text-transform: uppercase;
    white-space: nowrap;
  }

  .headline {
    position: absolute;
    left: 40px;
    top: 288px;
    font-family: "Bebas Neue", sans-serif;
    font-size: 104px;
    line-height: 95px;
    font-weight: 400;
    color: var(--teal);
    white-space: nowrap;
  }
  .headline .muted { color: var(--ink-grey); }

  .quiz-pitch {
    position: absolute;
    left: 50px;
    top: 860px;
    font-size: 42px;
    line-height: 55px;
    font-weight: 300;
    color: var(--white);
    white-space: nowrap;
  }
  .quiz-pitch strong { font-weight: 700; }

  .appointments {
    position: absolute;
    left: 838px;
    top: 1064px;
    white-space: nowrap;
  }
  .appointments-label {
    font-weight: 600;
    font-size: 23px;
    color: var(--dark-grey);
    line-height: 28px;
  }
  .appointments-phone {
    font-family: "Bebas Neue", sans-serif;
    font-size: 72px;
    line-height: 66px;
    letter-spacing: -1px;
    word-spacing: -6px;
    color: var(--dark-grey);
    margin-top: 4px;
  }
</style>
</head>
<body>
  <main class="ad">
    <div class="model-photo" role="img" aria-label="Photo of a smiling slim woman in a white sports top holding out the waistband of oversized blue jeans"></div>

    <svg class="shapes" viewBox="0 0 1200 1200" aria-hidden="true">
      <defs>
        <linearGradient id="greyBand" x1="0" y1="0" x2="1" y2="0">
          <stop offset="0" stop-color="#77787c"/>
          <stop offset="1" stop-color="#c3c5c9"/>
        </linearGradient>
        <linearGradient id="greyHill" x1="0" y1="0" x2="1" y2="0">
          <stop offset="0" stop-color="#b4b8be"/>
          <stop offset="1" stop-color="#cfd2d6"/>
        </linearGradient>
        <linearGradient id="tealWave" x1="0" y1="0" x2="0" y2="1">
          <stop offset="0" stop-color="#3fb1a8"/>
          <stop offset="1" stop-color="#0c746c"/>
        </linearGradient>
      </defs>
      <path class="grey-hill" d="M1200,291 C1090,296 1040,560 970,740 C930,840 860,880 700,930 L0,930 L0,1200 L1200,1200 Z" fill="url(#greyHill)"/>
      <path class="grey-hill-front" d="M1200,572 C1150,560 1120,640 1080,720 C1040,800 980,860 880,930 L1200,930 Z" fill="#bfc2c7" opacity="0.7"/>
      <path class="grey-band" d="M0,1000 L1200,1000 L1200,1200 L0,1200 Z" fill="url(#greyBand)"/>
      <path class="grey-band-blend" d="M0,920 L1200,880 L1200,1010 L0,1010 Z" fill="url(#greyBand)"/>
      <path class="teal-wave-glow" d="M760,900 C880,880 960,850 1015,783 C900,960 700,1110 420,1160 C600,1060 700,980 760,900 Z" fill="#14998f" opacity="0.45"/>
      <path class="teal-wave" d="M0,828 C80,780 180,742 300,758 C480,785 640,900 840,888 C910,884 960,850 1015,783 C900,960 700,1110 360,1166 C200,1182 80,1120 0,1066 Z" fill="url(#tealWave)"/>
    </svg>

    <header class="brand">
      <span class="brand-dot"></span>
      <div>
        <div class="brand-name">Merivale Bardsley</div>
        <div class="brand-role">General, Upper GI &amp; Bariatric Surgeon</div>
      </div>
    </header>

    <h1 class="headline">
      Curious about<br>
      <span class="muted">weight loss</span><br>
      surgery?
    </h1>

    <p class="quiz-pitch">
      This <strong>30 Second Quiz</strong><br>
      Will Tell You <strong>Which</strong><br>
      <strong>Procedure</strong> Will<br>
      Suit <strong>You Best....</strong>
    </p>

    <div class="appointments">
      <div class="appointments-label">FOR ALL APPOINTMENTS</div>
      <div class="appointments-phone">(03) 9000 4821</div>
    </div>
  </main>
</body>
</html>
```